Legal firm website redesign

Existing site for Sydney CBD lawyer needs clean and professional redesign - http://penfoldlaw.com.au

The site will be viewed by a wide range of users: businesses, individuals, referral partners and other lawyers.

Please see the list of must haves for further details

Target Market(s)

Businesses, individuals, referral partners and other lawyers

Industry/Entity Type

Lawyer

Requirements
Must have
• Prominent display of phone number.
List of services down the left hand side of the site (5x services or so).
Search box in header.
Please use the greys and blues from the existing header.
New header must include the wording "Efficiency - Fulfillment - Integrity - Teamwork"

```html
<!DOCTYPE html>
<html lang="en">
<head>
<meta charset="utf-8">
<title>Penfold Law</title>
<link rel="stylesheet" href="https://fonts.googleapis.com/css2?family=Kreon:wght@600&family=Marcellus&family=Tenor+Sans&family=PT+Sans:ital,wght@0,400;0,700;1,400&display=swap">
<style>
  :root {
    --header-grey: #5e5e5e;
    --band-grey: #dadada;
    --footer-grey: #3b3b3b;
    --blue-light: #10b0ea;
    --blue-dark: #0279c9;
    --blue-text: #1a95d3;
    --text: #555555;
    --text-dark: #333333;
    --orange: #e5620f;
    --tab-blue: #1a8ec6;
    --green: #5a8a2b;
    --tab-grey: #b4b4b4;
    --white: #ffffff;
    --rule: #c9c9c9;
  }
  * { margin: 0; padding: 0; box-sizing: border-box; }
  html, body { width: 1200px; height: 1015px; overflow: hidden; }
  body { position: relative; background: var(--white); font-family: "PT Sans", sans-serif; color: var(--text); }
  h2 { font-weight: 400; }

  .masthead { position: absolute; left: 0; top: 0; width: 1200px; height: 200px; background: var(--header-grey); }
  .service-band { position: absolute; left: 0; top: 200px; width: 1200px; height: 371px; background: var(--band-grey); }

  .brand { position: absolute; left: 94px; top: 56px; font-family: "Kreon", serif; font-weight: 600; font-size: 54px; color: var(--white); letter-spacing: -1px; }

  .contact { position: absolute; left: 840px; top: 56px; font-family: "Tenor Sans", sans-serif; color: var(--white); font-size: 21px; line-height: 28px; }
  .contact .value { color: #f1f1f1; }
  .contact .row { display: flex; }
  .contact .row .label { width: 102px; display: inline-block; }

  .main-nav { position: absolute; left: 56px; top: 169px; width: 1086px; height: 55px; border-radius: 4px;
    background: linear-gradient(to bottom, var(--blue-light), var(--blue-dark)); box-shadow: 0 3px 4px rgba(0,0,0,0.25); }
  .main-nav a { position: absolute; top: 17px; color: var(--white); font-weight: 700; font-size: 16px; text-decoration: none; }
  .main-nav .sep { position: absolute; top: 14px; width: 1px; height: 28px; background: rgba(255,255,255,0.3); }
  .search { position: absolute; left: 882px; top: 15px; width: 188px; height: 26px; border-radius: 13px; background: var(--white);
    box-shadow: inset 0 1px 2px rgba(0,0,0,0.3); font-style: italic; font-size: 13px; color: #333; padding: 4px 15px; }
  .search svg { position: absolute; right: 10px; top: 7px; }

  .services-title { position: absolute; left: 60px; top: 243px; font-size: 21px; color: var(--text-dark); }
  .services { position: absolute; left: 60px; top: 282px; width: 244px; list-style: none; }
  .services li { height: 39px; line-height: 38px; border-bottom: 1px solid var(--rule); font-size: 15px; color: var(--text); display: flex; align-items: center; }
  .services li:last-child { border-bottom: none; }
  .services li svg { margin-right: 6px; }

  .hero { position: absolute; left: 318px; top: 231px; width: 829px; height: 295px;
    background: linear-gradient(135deg, #f4ecdc 0%, #e8e4dc 40%, #f6f6f6 70%, #dcdcdc 100%); }
  .values { position: absolute; z-index: 2; left: 318px; top: 526px; width: 829px; height: 63px; display: flex; box-shadow: 0 6px 8px rgba(0,0,0,0.25); }
  .values div { height: 63px; display: flex; align-items: center; justify-content: center; font-family: "Marcellus", serif; font-size: 22px; color: var(--white); text-shadow: 0 1px 2px rgba(0,0,0,0.45); }
  .v-efficiency { width: 219px; background: linear-gradient(var(--orange), #c94e06); }
  .v-fulfillment { width: 223px; background: linear-gradient(var(--tab-blue), #0d75aa); }
  .v-integrity { width: 205px; background: linear-gradient(var(--green), #4a7621); }
  .v-teamwork { width: 182px; background: linear-gradient(#c4c4c4, var(--tab-grey)); }

  .slider-dots { position: absolute; left: 706px; top: 604px; display: flex; gap: 7px; }
  .slider-dots span { width: 14px; height: 14px; border-radius: 50%; background: linear-gradient(#d8d8d8, #555); border: 1px solid #333; }
  .slider-dots span.active { background: linear-gradient(#5cc3f0, #0b6fa8); }

  .welcome-title { position: absolute; left: 56px; top: 624px; font-size: 20px; color: var(--blue-text); }
  .welcome-photo { position: absolute; left: 56px; top: 665px; width: 239px; height: 159px; border: 1px solid #ddd; padding: 4px; background: var(--white); }
  .welcome-photo div { width: 100%; height: 100%; background: linear-gradient(135deg, #7c8c86, #c9d6cf 50%, #6f7d79); }
  .welcome-text { position: absolute; left: 322px; top: 656px; width: 490px; font-size: 12.5px; line-height: 27.4px; color: var(--text); }

  .news-col { position: absolute; z-index: 1; left: 827px; top: 589px; width: 320px; height: 342px; background: linear-gradient(to right, #eeeeee, #ffffff 25%); }
  .news-title { position: absolute; z-index: 2; left: 848px; top: 637px; font-size: 20px; color: var(--blue-text); }
  .news-item { position: absolute; z-index: 2; left: 850px; width: 290px; display: flex; }
  .news-item p { margin-left: 14px; font-size: 12.5px; line-height: 20px; color: var(--text); }
  .news-item time { display: block; font-style: italic; font-size: 12px; color: #222; }
  .news-divider { position: absolute; z-index: 2; left: 848px; top: 757px; width: 288px; border-top: 1px dashed #aaa; }

  .site-footer { position: absolute; left: 0; top: 931px; width: 1200px; height: 84px; background: var(--footer-grey); }
  .footer-links { position: absolute; left: 63px; top: 18px; font-size: 12.5px; line-height: 20px; color: #bdbdbd; }
  .connect { position: absolute; left: 745px; top: 23px; font-size: 20px; color: #bbbbbb; }
  .social { position: absolute; top: 22px; width: 30px; height: 30px; border-radius: 4px; background: #6d6d6d; }
</style>
</head>
<body>
  <header class="masthead">
    <div class="brand">penfold law</div>
    <div class="contact">
      <div class="row"><span class="label">CALL US:</span><span class="value">(02) 9460 3320</span></div>
      <div class="row"><span class="label"></span><span class="value">(02) 9460 3321</span></div>
      <div class="row"><span class="label">EMAIL&nbsp;&nbsp;&nbsp;:</span><span class="value">info@penfoldlaw.com.au</span></div>
    </div>
  </header>
  <div class="service-band"></div>

  <nav class="main-nav">
    <a href="#" style="left:38px">Home</a>
    <span class="sep" style="left:96px"></span>
    <a href="#" style="left:120px">About Us</a>
    <span class="sep" style="left:198px"></span>
    <a href="#" style="left:212px">Areas of Law</a>
    <span class="sep" style="left:314px"></span>
    <a href="#" style="left:329px">Publications</a>
    <span class="sep" style="left:430px"></span>
    <a href="#" style="left:448px">Contact</a>
    <div class="search">Search
      <svg width="13" height="13" viewBox="0 0 13 13"><circle cx="5" cy="5" r="3.8" fill="none" stroke="#888" stroke-width="1.5"/><line x1="8" y1="8" x2="12" y2="12" stroke="#888" stroke-width="2"/></svg>
    </div>
  </nav>

  <h2 class="services-title">Our Service</h2>
  <ul class="services">
    <li><svg width="14" height="8" viewBox="0 0 14 8"><rect x="0" y="2" width="6" height="4" fill="#777"/><path d="M6 1h5l3 3-3 3H6z" fill="#777"/></svg>Financing</li>
    <li><svg width="14" height="8" viewBox="0 0 14 8"><rect x="0" y="2" width="6" height="4" fill="#777"/><path d="M6 1h5l3 3-3 3H6z" fill="#777"/></svg>Leasing</li>
    <li><svg width="14" height="8" viewBox="0 0 14 8"><rect x="0" y="2" width="6" height="4" fill="#777"/><path d="M6 1h5l3 3-3 3H6z" fill="#777"/></svg>Property transactions</li>
    <li><svg width="14" height="8" viewBox="0 0 14 8"><rect x="0" y="2" width="6" height="4" fill="#777"/><path d="M6 1h5l3 3-3 3H6z" fill="#777"/></svg>Joint ventures</li>
    <li><svg width="14" height="8" viewBox="0 0 14 8"><rect x="0" y="2" width="6" height="4" fill="#777"/><path d="M6 1h5l3 3-3 3H6z" fill="#777"/></svg>Business restructuring</li>
    <li><svg width="14" height="8" viewBox="0 0 14 8"><rect x="0" y="2" width="6" height="4" fill="#777"/><path d="M6 1h5l3 3-3 3H6z" fill="#777"/></svg>Contract review and advice</li>
    <li><svg width="14" height="8" viewBox="0 0 14 8"><rect x="0" y="2" width="6" height="4" fill="#777"/><path d="M6 1h5l3 3-3 3H6z" fill="#777"/></svg>Employment Law Documentation</li>
  </ul>

  <div class="hero" role="img" aria-label="Close-up photo of a gold pen tip over a signed legal document"></div>
  <div class="values">
    <div class="v-efficiency">EFFICIENCY</div>
    <div class="v-fulfillment">FULLFILLMENT</div>
    <div class="v-integrity">INTEGRITY</div>
    <div class="v-teamwork">TEAM WORK</div>
  </div>
  <div class="slider-dots"><span></span><span class="active"></span><span></span><span></span></div>

  <div class="news-col"></div>

  <h2 class="welcome-title">Welcome To Penfold Law</h2>
  <div class="welcome-photo"><div role="img" aria-label="Photo of the firm's reception desk with staff"></div></div>
  <div class="welcome-text">
    <p>Penfold Law is a dynamic commercial law firm in the CBD of Sydney providing services to corporate, small business and private clients.</p>
    <p>Penfold Law brings together over 30 years of experience in legal practice.</p>
    <p>The strong focus of the firm is on commercial law and estate planning.</p>
    <p>Penfold Law is committed to providing quality legal services in helping its clients achieve their objectives by providing a proactive understanding of its clients' businesses and creative legal solutions.</p>
  </div>

  <h2 class="news-title">Latest News</h2>
  <div class="news-item" style="top:682px">
    <svg width="26" height="30" viewBox="0 0 26 30"><rect x="1" y="4" width="24" height="25" rx="2" fill="#f4f4f4" stroke="#aaa"/><rect x="1" y="4" width="24" height="6" fill="#bbb"/><rect x="6" y="1" width="2" height="6" fill="#888"/><rect x="18" y="1" width="2" height="6" fill="#888"/><text x="13" y="25" font-size="11" text-anchor="middle" fill="#888" font-family="PT Sans, sans-serif">27</text></svg>
    <p>It is a long established fact that a reader will be distracted by the readable content .<time>Mar 9, 2012</time></p>
  </div>
  <div class="news-divider"></div>
  <div class="news-item" style="top:775px">
    <svg width="26" height="30" viewBox="0 0 26 30"><rect x="1" y="4" width="24" height="25" rx="2" fill="#f4f4f4" stroke="#aaa"/><rect x="1" y="4" width="24" height="6" fill="#bbb"/><rect x="6" y="1" width="2" height="6" fill="#888"/><rect x="18" y="1" width="2" height="6" fill="#888"/><text x="13" y="25" font-size="11" text-anchor="middle" fill="#888" font-family="PT Sans, sans-serif">27</text></svg>
    <p>It is a long established fact that a reader will be distracted by the readable content .<time>Mar 9, 2012</time></p>
  </div>

  <footer class="site-footer">
    <div class="footer-links">Home | About Us | Area of Law | Our People | Publication | Contact<br>Copyright@2012&nbsp; www.penfoldlaw.com.au</div>
    <div class="connect">Connect With Us</div>
    <span class="social" style="left:911px" role="img" aria-label="Social network link"></span>
    <span class="social" style="left:955px" role="img" aria-label="Social network link"></span>
    <span class="social" style="left:1001px" role="img" aria-label="News feed link"></span>
    <span class="social" style="left:1046px" role="img" aria-label="Social network link"></span>
    <span class="social" style="left:1092px" role="img" aria-label="Social network link"></span>
  </footer>
</body>
</html>
```